Marcus Penhale Logo and Wine Lable design

• What I am looking for is a packaging design to represent my product. The message I am looking for is a representation of western royal culture. Expensive and elegant. I want the label to look old, like from ancient times, feels like full of story, yet outstanding on the shelf among others. Special printing technique or paper can be used for an aged appearance.
• The packaging should include the logo, bottle, and the box that contains 12 bottle of wine.
• Shiraz
• Brand name Marcus Penhale must be included.
• Logo design should follow the same concept as above.
• There must be two labels, one on the front and one on the back of the bottle. The front label will carry most of the graphical impact.
• The back label should include some text for the wine, this could be anything, it is up to the design to present the story or testing of the wine in the test, which should also follow the concept above.
• The back label must have a standard space for barcode
• The label of packaging solution should also compline with the Vintage Record Scheme of Cellar Board Oceania.
• Final artwork ready for the printer should be provided in PDF format on CD, and include all fonts, images etc needed for printing

Reason: Hi guys, I am extending the deadline of this project as i am still seeking the design that could fulfill all my requirements, most important of all, as wine label, designs need to compliance with the Australia wine label requirement. in the extension, I will provide feed back to my designers proactively to find the right design that fits my requirement. Tom

Reason: waiting on the finalization on same designs

Industry/Entity Type

Printer

```html
<!DOCTYPE html>
<html lang="en">
<head>
<meta charset="utf-8">
<title>Marcus Penhale Shiraz – Label Variants</title>
<link href="https://fonts.googleapis.com/css2?family=Jost:wght@400;500&display=swap" rel="stylesheet">
<style>
  :root {
    --night: #060606;
    --night-grid: #0c0c0c;
    --cream-center: #fffbe3;
    --cream-edge: #eee0b4;
    --gold: #c8a550;
    --gold-light: #e9d27e;
    --gold-soft: rgba(200, 165, 80, 0.22);
    --ink: #3b352d;
    --ink-soft: rgba(59, 53, 45, 0.14);
    --claret: #d2352c;
  }
  * { margin: 0; padding: 0; box-sizing: border-box; }
  html, body {
    width: 1200px;
    height: 766px;
    overflow: hidden;
    background: #ffffff;
  }
  .label-sheet {
    display: flex;
    width: 1200px;
    height: 766px;
    font-family: "Jost", "Futura", sans-serif;
  }
  .label {
    position: relative;
    width: 600px;
    height: 766px;
    text-align: center;
  }
  .label--night {
    background-color: var(--night);
    background-image:
      linear-gradient(var(--night-grid) 1px, transparent 1px),
      linear-gradient(90deg, var(--night-grid) 1px, transparent 1px);
    background-size: 8px 8px;
    --accent: var(--gold);
    --accent-soft: var(--gold-soft);
    --brand: var(--gold);
    --varietal: var(--gold-light);
  }
  .label--cream {
    background: radial-gradient(ellipse at 50% 50%, var(--cream-center) 0%, var(--cream-center) 35%, var(--cream-edge) 100%);
    --accent: var(--ink);
    --accent-soft: var(--ink-soft);
    --brand: var(--ink);
    --varietal: var(--claret);
  }
  .label__frame {
    position: absolute;
    left: 0; top: 0;
    width: 600px; height: 766px;
  }
  .label__tagline {
    position: absolute;
    top: 162px; left: 0; right: 0;
    font-size: 11px;
    letter-spacing: 3px;
    color: var(--accent);
    font-weight: 400;
  }
  .label__brand {
    position: absolute;
    top: 238px; left: 0; right: 0;
    font-size: 38px;
    line-height: 40px;
    font-weight: 500;
    color: var(--brand);
  }
  .label__varietal {
    position: absolute;
    top: 396px; left: 0; right: 0;
    padding-left: 13px;
    font-size: 38px;
    font-weight: 400;
    letter-spacing: 13px;
    color: var(--varietal);
  }
  .label__vintage {
    position: absolute;
    top: 593px; left: 0; right: 0;
    padding-left: 3px;
    font-size: 11px;
    letter-spacing: 3px;
    color: var(--accent);
  }
</style>
</head>
<body>
<main class="label-sheet">

  <section class="label label--night">
    <svg class="label__frame" viewBox="0 0 600 766">
      <g stroke="var(--accent)" stroke-width="1.2" fill="none">
        <polyline points="104,220 104,92 496,92 496,220"/>
        <polyline points="104,500 104,650 496,650 496,500"/>
      </g>
      <rect role="img" aria-label="Scrolled flourish ornament, top left corner" x="110" y="98" width="56" height="104" rx="28" fill="var(--accent-soft)"/>
      <rect role="img" aria-label="Scrolled flourish ornament, top right corner" x="434" y="98" width="56" height="104" rx="28" fill="var(--accent-soft)"/>
      <rect role="img" aria-label="Scrolled flourish ornament, bottom left corner" x="110" y="520" width="56" height="124" rx="28" fill="var(--accent-soft)"/>
      <rect role="img" aria-label="Scrolled flourish ornament, bottom right corner" x="434" y="520" width="56" height="124" rx="28" fill="var(--accent-soft)"/>
    </svg>
    <p class="label__tagline">western royal culture</p>
    <h1 class="label__brand">Marcus<br>Penhale</h1>
    <p class="label__varietal">SHIRAZ</p>
    <p class="label__vintage">2012</p>
  </section>

  <section class="label label--cream">
    <svg class="label__frame" viewBox="0 0 600 766">
      <g stroke="var(--accent)" stroke-width="1.2" fill="none">
        <polyline points="104,220 104,92 496,92 496,220"/>
        <polyline points="104,500 104,650 496,650 496,500"/>
      </g>
      <rect role="img" aria-label="Scrolled flourish ornament, top left corner" x="110" y="98" width="56" height="104" rx="28" fill="var(--accent-soft)"/>
      <rect role="img" aria-label="Scrolled flourish ornament, top right corner" x="434" y="98" width="56" height="104" rx="28" fill="var(--accent-soft)"/>
      <rect role="img" aria-label="Scrolled flourish ornament, bottom left corner" x="110" y="520" width="56" height="124" rx="28" fill="var(--accent-soft)"/>
      <rect role="img" aria-label="Scrolled flourish ornament, bottom right corner" x="434" y="520" width="56" height="124" rx="28" fill="var(--accent-soft)"/>
    </svg>
    <p class="label__tagline">western royal culture</p>
    <h2 class="label__brand">Marcus<br>Penhale</h2>
    <p class="label__varietal">SHIRAZ</p>
    <p class="label__vintage">2012</p>
  </section>

</main>
</body>
</html>
```